Stainless Steel Business Card

I have a fiber laser and want to highlight its capabilities in a business card. On the card I want

Brisler Systems
Martin Pelko
martin@mpelkoworks.com
417-555-0136

This will be cut / engraved on stainless steel. I want the Brisler Systems to be prominent with laser cut font so that there are no dropouts on the O and A's. My name email and phone number should be engraved black. I would like some cool geometric patterns to cutout on the card to highlight the capabilities of my machine. I will need to files in the end either SVG or dxf of the engrave portion and the cut portion.

```html
<!DOCTYPE html>
<html lang="en">
<head>
<meta charset="utf-8">
<title>Brisler Systems – Business Card</title>
<link href="https://fonts.googleapis.com/css2?family=Poppins:wght@400;500;600&display=swap" rel="stylesheet">
<style>
  :root {
    --page-bg: #e9e6e1;
    --card-black: #050505;
    --panel-dark: #1b1b1b;
    --panel-mid: #0f0f0f;
    --brand-red: #d71f26;
    --text-light: #f1f1f1;
    --ring-grey: #e4e4e4;
  }
  * { margin: 0; padding: 0; box-sizing: border-box; }
  html, body {
    width: 1189px;
    height: 1200px;
    overflow: hidden;
    background: var(--page-bg);
    font-family: "Poppins", sans-serif;
  }
  .card {
    position: absolute;
    left: 169px;
    width: 851px;
    height: 485px;
    border-radius: 40px;
    background: var(--card-black);
    overflow: hidden;
    box-shadow: 0 10px 24px rgba(0,0,0,0.35);
  }
  .card--front { top: 112px; }
  .card--back { top: 641px; }

  .card__panel {
    position: absolute;
    left: 0;
    right: 0;
    background: radial-gradient(ellipse at 50% 45%, var(--panel-dark) 0%, var(--panel-mid) 70%, var(--card-black) 100%);
  }
  .card--front .card__panel { top: 51px; height: 383px; }
  .card--back .card__panel { top: 114px; height: 263px; }

  .card__rule {
    position: absolute;
    left: 0;
    right: 0;
    height: 6px;
    background: var(--brand-red);
  }
  .card--front .card__rule--top { top: 51px; }
  .card--front .card__rule--bottom { top: 428px; }
  .card--back .card__rule--top { top: 114px; }
  .card--back .card__rule--bottom { top: 371px; }

  .brand-name {
    position: absolute;
    color: var(--brand-red);
    font-weight: 500;
    text-transform: uppercase;
    white-space: nowrap;
    text-align: center;
  }
  .card--front .brand-name {
    left: 56px;
    width: 350px;
    top: 128px;
    font-size: 30px;
    letter-spacing: 5px;
  }
  .card--back .brand-name {
    left: 0;
    width: 851px;
    top: 205px;
    font-size: 56px;
    letter-spacing: 12px;
  }

  .contact {
    position: absolute;
    left: 56px;
    width: 350px;
    text-align: center;
    color: var(--text-light);
  }
  .contact__name {
    position: absolute;
    top: 222px;
    width: 100%;
    color: var(--brand-red);
    font-weight: 600;
    font-size: 28px;
    line-height: 1.1;
  }
  .contact__role {
    position: absolute;
    top: 252px;
    width: 100%;
    font-size: 17px;
  }
  .contact__phone {
    position: absolute;
    top: 297px;
    width: 100%;
    font-size: 20px;
  }
  .contact__email {
    position: absolute;
    top: 326px;
    width: 100%;
    font-size: 20px;
  }

  .emblem {
    position: absolute;
    left: 521px;
    top: 124px;
    width: 236px;
    height: 236px;
  }
</style>
</head>
<body>

  <section class="card card--front">
    <div class="card__panel"></div>
    <div class="card__rule card__rule--top"></div>
    <div class="card__rule card__rule--bottom"></div>

    <div class="brand-name">Brisler Systems</div>

    <div class="contact">
      <div class="contact__name">MARTIN PELKO</div>
      <div class="contact__role">Manager</div>
      <div class="contact__phone">417-555-0136</div>
      <div class="contact__email">martin@mpelkoworks.com</div>
    </div>

    <svg class="emblem" viewBox="0 0 236 236" aria-hidden="true">
      <circle cx="118" cy="118" r="111" fill="none" stroke="var(--ring-grey)" stroke-width="7"/>
    </svg>
  </section>

  <section class="card card--back">
    <div class="card__panel"></div>
    <div class="card__rule card__rule--top"></div>
    <div class="card__rule card__rule--bottom"></div>

    <div class="brand-name">Brisler Systems</div>
  </section>

</body>
</html>
```